Brovan Equipment Sales & Rentals

We are an independent equipment dealership located in the upstate of South Carolina. Our services include Equipment Sales, Equipment Rentals, Metal Sales, and Industrial Supplies.

I have attached our logos and a few billboards that we like as examples for inspiration. Thank you!

Phone Number 864-555-0172

Website link if you want to check out our page.
https://www.brovanmachinery.example

```html
<!DOCTYPE html>
<html lang="en">
<head>
<meta charset="utf-8">
<title>Brovan Equipment Sales &amp; Rentals – Billboard</title>
<link href="https://fonts.googleapis.com/css2?family=Saira:ital,wght@0,800;1,400;1,700;1,800&display=swap" rel="stylesheet">
<style>
  :root {
    --red: #f50a0a;
    --red-deep: #c8000a;
    --ink: #111111;
    --white: #ffffff;
    --stage: #ececec;
    --dust: #c9a57a;
  }
  * { box-sizing: border-box; margin: 0; padding: 0; }
  html, body { width: 976px; height: 1200px; overflow: hidden; }
  body {
    background: var(--stage);
    font-family: "Saira", sans-serif;
    position: relative;
  }
  .billboard {
    position: absolute;
    left: 28px; top: 370px;
    width: 920px; height: 460px;
    background: var(--white);
    overflow: hidden;
    box-shadow: -6px 8px 14px rgba(0,0,0,.35);
  }
  .hero-photo {
    position: absolute;
    left: 382px; top: 0; width: 538px; height: 390px;
    background:
      linear-gradient(90deg, var(--white) 0%, rgba(255,255,255,0) 28%),
      linear-gradient(180deg, #8fa8bf 0%, #e9e3d8 45%, #d7b27a 65%, var(--dust) 82%, #b89a78 100%);
  }
  .brand-name {
    position: absolute;
    left: 48px; top: 22px;
    font-weight: 800; font-style: normal;
    font-size: 88px; line-height: 1;
    color: var(--ink);
    letter-spacing: 1px;
  }
  .brand-name::before {
    content: ""; display: inline-block;
    width: 44px; height: 44px; background: var(--red);
    margin-right: 14px; vertical-align: 6px;
  }
  .headline {
    position: absolute; left: 46px; top: 122px;
    font-weight: 800; font-style: italic;
    font-size: 29px; line-height: 39px;
    color: var(--ink); text-transform: uppercase;
  }
  .location {
    position: absolute; left: 46px; top: 203px;
    font-weight: 400; font-style: italic; font-size: 17px;
    color: var(--ink);
  }
  .location em { color: var(--red); font-style: italic; }
  .services-tab {
    position: absolute; left: 0; top: 249px; width: 222px; height: 37px;
    background: linear-gradient(90deg, #3a3a3a, var(--ink));
    clip-path: polygon(0 0, 190px 0, 222px 37px, 0 37px);
    color: var(--white); font-weight: 800; font-style: italic; font-size: 20px;
    padding: 4px 0 0 47px; letter-spacing: .5px;
  }
  .services-panel {
    position: absolute; left: 0; top: 286px; width: 464px; height: 174px;
    background: linear-gradient(90deg, var(--red-deep) 0%, var(--red) 60%);
    clip-path: polygon(0 0, 367px 0, 464px 174px, 0 174px);
  }
  .service {
    position: absolute; display: flex; align-items: center; gap: 10px;
    color: var(--white); font-weight: 700; font-style: italic;
    font-size: 21px; line-height: 23px;
  }
  .service svg { width: 34px; height: 34px; flex: none; }
  .service--sales { left: 48px; top: 319px; }
  .service--rentals { left: 48px; top: 386px; }
  .service--metal { left: 234px; top: 319px; }
  .service--supplies { left: 234px; top: 386px; }
  .divider { position: absolute; top: 375px; height: 2px; background: var(--white); }
  .divider--left { left: 48px; width: 147px; }
  .divider--right { left: 234px; width: 141px; }
  .web-band {
    position: absolute; left: 478px; top: 39px; width: 442px; height: 46px;
    background: var(--red);
    clip-path: polygon(0 0, 442px 0, 442px 46px, 18px 46px);
    color: var(--white); font-weight: 800; font-style: italic;
    font-size: 24px; line-height: 46px; padding-left: 32px;
    white-space: nowrap; letter-spacing: 0;
  }
  .phone-band {
    position: absolute; left: 425px; top: 388px; width: 495px; height: 72px;
    background: var(--ink);
    clip-path: polygon(0 0, 495px 0, 495px 72px, 40px 72px);
    display: flex; align-items: center; gap: 14px; padding-left: 110px;
    color: var(--white); font-weight: 800; font-style: italic; font-size: 44px;
  }
  .phone-band::after {
    content: ""; position: absolute; right: 0; top: 0; width: 40px; height: 72px;
    background: var(--red); clip-path: polygon(0 0, 40px 0, 40px 72px);
  }
  .phone-band svg { width: 34px; height: 34px; }
</style>
</head>
<body>
  <main class="billboard">
    <div class="hero-photo" role="img" aria-label="Photo of yellow excavators and a dozer on a dusty job site under a bright sky"></div>

    <div class="brand-name">BROVAN</div>
    <h1 class="headline">We are an independent<br>equipment dealership</h1>
    <p class="location">Located in the upstate of <em>South Carolina.</em></p>

    <div class="web-band">www.brovanmachinery.example</div>

    <div class="services-tab">OUR SERVICES</div>
    <div class="services-panel"></div>

    <div class="service service--sales">
      <svg viewBox="0 0 34 34" fill="none" stroke="#fff" stroke-width="1.6"><rect x="3" y="22" width="24" height="8" rx="4"/><rect x="8" y="13" width="10" height="9"/><path d="M18 14l8-8 4 10"/></svg>
      <span>Equipment<br>Sales</span>
    </div>
    <div class="service service--rentals">
      <svg viewBox="0 0 34 34" fill="none" stroke="#fff" stroke-width="1.6"><rect x="3" y="22" width="24" height="8" rx="4"/><rect x="6" y="11" width="12" height="11"/><path d="M18 12l8-7 5 11"/><circle cx="27" cy="24" r="4"/></svg>
      <span>Equipment<br>Rentals</span>
    </div>
    <div class="service service--metal">
      <svg viewBox="0 0 34 34" fill="none" stroke="#fff" stroke-width="1.6"><path d="M4 20l14-14h12L16 20z"/><path d="M4 20v10h12V20M16 30l14-14V6"/></svg>
      <span>Metal<br>Sales</span>
    </div>
    <div class="service service--supplies">
      <svg viewBox="0 0 34 34" fill="none" stroke="#fff" stroke-width="1.6"><rect x="3" y="16" width="12" height="10"/><rect x="16" y="20" width="13" height="8"/><circle cx="24" cy="10" r="5"/><path d="M3 16l4-5 4 5"/></svg>
      <span>Industrial<br>Supplies</span>
    </div>
    <div class="divider divider--left"></div>
    <div class="divider divider--right"></div>

    <div class="phone-band">
      <svg viewBox="0 0 24 24" fill="#fff"><path d="M6.6 10.8a15 15 0 006.6 6.6l2.2-2.2a1 1 0 011-.25 11.4 11.4 0 003.6.57 1 1 0 011 1V20a1 1 0 01-1 1A17 17 0 013 4a1 1 0 011-1h3.5a1 1 0 011 1c0 1.25.2 2.45.57 3.57a1 1 0 01-.25 1z"/><path d="M14 2.5a8 8 0 017.5 7.5h-1.6A6.4 6.4 0 0014 4.1zM14 5.8a4.8 4.8 0 014.2 4.2h-1.6A3.2 3.2 0 0014 7.4z"/></svg>
      <span>864-555-0172</span>
    </div>
  </main>
</body>
</html>
```